Business Card for New Business

Please design a business card using our logo and font files. This is only one card for one person, as listed in details section.

Contact Information for Business Card

Dale Vornhuser

Phone 240.815.3926
Cell 703.461.8075
Email dale@morlenbay.com

www.morlenbay.com

Address
31800 Pinecrest Lane #412
Damascus, MD 20879

Font styles to use
Sans Serif

Requirements
Must have
• Information listed in detail section. Must be standard card size.

```html
<!DOCTYPE html>
<html lang="en">
<head>
<meta charset="utf-8">
<title>Morlenbay Productions – Business Card</title>
<link href="https://fonts.googleapis.com/css2?family=Quicksand:wght@400;500;600&display=swap" rel="stylesheet">
<style>
  :root {
    --backdrop: #2b2b2d;
    --card-white: #ffffff;
    --card-black: #0c0c0d;
    --ink-dark: #2a2627;
    --ink-light: #f2f2f2;
    --ink-muted: #6b6b6b;
    --accent-orange: #e8703a;
    --accent-red: #d8412f;
    --mark-grey: #dcdcdc;
  }
  * { box-sizing: border-box; margin: 0; padding: 0; }
  html, body { width: 1200px; height: 900px; overflow: hidden; }
  body {
    background: var(--backdrop);
    font-family: "Quicksand", sans-serif;
    position: relative;
  }
  .card {
    position: absolute;
    width: 525px;
    height: 300px;
    border-radius: 16px;
    overflow: hidden;
    box-shadow: 0 18px 40px rgba(0,0,0,0.45);
  }
  /* front */
  .card-front { left: 80px; top: 130px; background: var(--card-white); }
  .front-brand {
    position: absolute; left: 0; right: 0; top: 100px;
    display: flex; align-items: center; justify-content: center; gap: 12px;
  }
  .brand-dot {
    width: 40px; height: 40px; border-radius: 50%;
    background: var(--accent-red);
  }
  .front-brand .brand-name {
    font-size: 44px; font-weight: 600; color: var(--ink-dark); letter-spacing: 1px;
  }
  .front-web {
    position: absolute; left: 0; right: 0; top: 236px; text-align: center;
    font-size: 13px; font-weight: 600; color: var(--ink-dark);
  }
  .front-web .web-domain { color: var(--accent-red); }
  /* back */
  .card-back { left: 595px; top: 470px; background: var(--card-black); }
  .back-decoration {
    position: absolute; right: -70px; top: 120px;
    width: 240px; height: 240px; border-radius: 50%;
    background: var(--accent-red);
  }
  .back-brand { position: absolute; right: 40px; top: 30px; text-align: right; }
  .back-brand-row { display: flex; align-items: center; gap: 8px; justify-content: flex-end; }
  .back-brand .brand-dot { width: 22px; height: 22px; }
  .back-brand .brand-name { font-size: 34px; font-weight: 500; color: var(--accent-orange); line-height: 1; }
  .back-brand .brand-sub {
    font-size: 11px; letter-spacing: 7px; color: var(--ink-muted); margin-top: 4px;
  }
  .person { position: absolute; left: 40px; top: 112px; }
  .person-name {
    font-size: 14px; font-weight: 600; color: var(--accent-orange);
    text-transform: uppercase; letter-spacing: 0.5px;
  }
  .person-role { font-size: 13px; color: var(--ink-light); margin-top: 2px; }
  .contact { position: absolute; left: 40px; top: 178px; color: var(--ink-light); font-size: 12.5px; }
  .address { line-height: 1.35; margin-bottom: 6px; }
  .contact-list { list-style: none; }
  .contact-list li { display: flex; align-items: center; gap: 10px; line-height: 1.55; }
  .contact-list svg { width: 11px; height: 11px; fill: none; stroke: var(--accent-orange); stroke-width: 2; flex: none; }
  .contact-list .web-domain { color: var(--accent-red); }
</style>
</head>
<body>
  <section class="card card-front">
    <div class="front-brand">
      <span class="brand-dot"></span>
      <span class="brand-name">morlenbay</span>
    </div>
    <p class="front-web">www.<span class="web-domain">morlenbay.com</span></p>
  </section>

  <section class="card card-back">
    <div class="back-decoration"></div>
    <div class="back-brand">
      <div class="back-brand-row">
        <span class="brand-dot"></span>
        <span class="brand-name">morlenbay</span>
      </div>
      <div class="brand-sub">PRODUCTIONS</div>
    </div>
    <div class="person">
      <p class="person-name">Dale Vornhuser</p>
      <p class="person-role">Your Position</p>
    </div>
    <div class="contact">
      <p class="address">31800 Pinecrest Lane #412<br>Damascus, MD 20879</p>
      <ul class="contact-list">
        <li><svg viewBox="0 0 12 12"><path d="M1 4c2-3 8-3 10 0M3 5h6l1 5H2z"/></svg>240.815.3926</li>
        <li><svg viewBox="0 0 12 12"><rect x="3" y="1" width="6" height="10" rx="1"/></svg>703.461.8075</li>
        <li><svg viewBox="0 0 12 12"><path d="M1 6l10-5-4 10-1-4z"/></svg>dale@morlenbay.com</li>
        <li><svg viewBox="0 0 12 12"><circle cx="6" cy="6" r="5"/><path d="M1 6h10M6 1c-3 3-3 7 0 10M6 1c3 3 3 7 0 10"/></svg><span>www.<span class="web-domain">morlenbay.com</span></span></li>
      </ul>
    </div>
  </section>
</body>
</html>
```